Become a Mentor - For Musicians, Artists, Producers and Teachers

Here is the full creative brief:

https://files.plenwick.com/sheets/d/4kTqpLm8Wz_2RNa7Hc3Xv91Jd0Gb5YeUsQ6fNo8rTpxa/view?mode=shared

Here is the background image file: https://www.trovecrate.com/sh/83jbwtrmq5dkx2u/BBHn4k7QTf2ZpLeXX-wr9MUHe?dl=0

LOGO:
https://www.trovecrate.com/sh/k472rufmpdo9b6w/BBKLe3RtHY5J-sFQnLZw7Ggma?dl=0

```html
<!DOCTYPE html>
<html lang="en">
<head>
<meta charset="utf-8">
<title>Become a Mentor – Meridian School of Music</title>
<link rel="stylesheet" href="https://fonts.googleapis.com/css2?family=Barlow+Semi+Condensed:wght@300;500;600;700&display=swap">
<style>
  :root {
    --purple: #3b1e6e;
    --blue: #1aa7ea;
    --orange: #f6a83b;
    --black: #000000;
    --white: #ffffff;
    --page: #ffffff;
    --photo-light: #6e6258;
    --photo-mid: #3d3733;
    --photo-dark: #211e1c;
  }
  * { box-sizing: border-box; margin: 0; padding: 0; }
  html, body {
    width: 1200px; height: 917px; overflow: hidden;
    background: var(--page);
    font-family: "Barlow Semi Condensed", "Arial Narrow", sans-serif;
  }
  .stage {
    position: absolute; left: 0; top: 7px;
    width: 1050px; height: 790px;
    transform: scale(1.1429); transform-origin: 0 0;
  }
  .ad { position: absolute; overflow: hidden; background: var(--black); }
  .ad--portrait { left: 28px; top: 28px; width: 528px; height: 742px; }
  .ad--square { left: 578px; top: 28px; width: 450px; height: 450px; }
  .ad--banner { left: 578px; top: 498px; width: 442px; height: 164px; }

  .layer { position: absolute; inset: 0; }
  .band-purple { background: var(--purple); }
  .rule-blue { background: var(--blue); }
  .rule-orange { background: var(--orange); }
  .rule-white { background: var(--white); }
  .band-black { background: var(--black); }
  .photo {
    background:
      radial-gradient(ellipse at 78% 40%, rgba(120,70,60,.55), transparent 45%),
      radial-gradient(ellipse at 25% 55%, rgba(200,190,175,.45), transparent 40%),
      linear-gradient(100deg, var(--photo-light), var(--photo-mid) 50%, var(--photo-dark));
  }

  .apply {
    position: absolute; top: 0; background: var(--blue); color: var(--white);
    display: flex; flex-direction: column; align-items: center; justify-content: center;
    line-height: 1;
  }
  .apply__light { font-weight: 300; }
  .apply__bold { font-weight: 700; }

  .headline {
    position: absolute; color: var(--white); font-weight: 600;
    text-transform: uppercase; line-height: 1; white-space: nowrap;
    transform-origin: left top;
  }
  .headline span { display: block; }
  .tagline {
    position: absolute; color: var(--orange); font-weight: 600;
    text-transform: uppercase; line-height: 1.15; transform-origin: left top;
  }
  .career {
    position: absolute; color: var(--white); font-weight: 600;
    text-transform: uppercase; line-height: 1; white-space: nowrap;
    transform-origin: left bottom;
    text-shadow: 0 2px 6px rgba(0,0,0,.45);
  }
  .audience {
    position: absolute; color: var(--white); font-weight: 600;
    text-transform: uppercase; white-space: nowrap;
  }
  .contacts { position: absolute; list-style: none; }
  .contacts li {
    display: flex; align-items: center; color: var(--blue);
    font-weight: 500; text-transform: uppercase; white-space: nowrap;
  }
  .contacts--banner li { color: var(--white); }
  .contacts svg { flex: none; }
  .brand {
    position: absolute; color: var(--white); font-weight: 600;
    text-transform: uppercase; text-align: center; line-height: 1.05;
  }
</style>
</head>
<body>
<svg width="0" height="0" style="position:absolute" aria-hidden="true">
  <defs>
    <symbol id="icon-phone" viewBox="0 0 20 20">
      <circle cx="10" cy="10" r="8.6" fill="none" stroke="#fff" stroke-width="1.4"/>
      <path d="M7 5.6l1.6-.3 1 2.3-1 .8a6 6 0 0 0 2.9 2.9l.8-1 2.3 1-.3 1.6c-.2.5-.7.8-1.3.7A8 8 0 0 1 6.3 6.9c0-.6.2-1.1.7-1.3z" fill="#fff"/>
    </symbol>
    <symbol id="icon-mail" viewBox="0 0 20 20">
      <circle cx="10" cy="10" r="8.6" fill="none" stroke="#fff" stroke-width="1.4"/>
      <rect x="5.5" y="6.8" width="9" height="6.4" fill="#fff"/>
      <path d="M5.5 7l4.5 3.4L14.5 7" fill="none" stroke="#000" stroke-width="1"/>
    </symbol>
    <symbol id="icon-web" viewBox="0 0 20 20">
      <circle cx="10" cy="10" r="8.6" fill="none" stroke="#fff" stroke-width="1.4"/>
      <circle cx="10" cy="10" r="4.6" fill="none" stroke="#fff" stroke-width="1.2"/>
      <path d="M5.4 10h9.2M10 5.4c-2 2.6-2 6.6 0 9.2M10 5.4c2 2.6 2 6.6 0 9.2" fill="none" stroke="#fff" stroke-width="1"/>
    </symbol>
  </defs>
</svg>

<main class="stage">

  <!-- Portrait poster -->
  <section class="ad ad--portrait">
    <div class="layer photo" role="img" aria-label="Photo of two young musicians talking at a mixing desk in a recording studio"
         style="clip-path:polygon(0 230px,528px 186px,528px 566px,0 602px)"></div>
    <div class="layer band-purple" style="clip-path:polygon(0 0,528px 0,528px 180px,0 222px)"></div>
    <div class="layer rule-blue" style="clip-path:polygon(0 222px,528px 180px,528px 188px,0 231px)"></div>
    <div class="layer rule-white" style="clip-path:polygon(232px 482px,528px 458px,528px 465px,232px 489px)"></div>
    <div class="layer rule-orange" style="clip-path:polygon(232px 489px,528px 465px,528px 469px,232px 493px)"></div>
    <div class="layer rule-blue" style="clip-path:polygon(0 569px,380px 537px,380px 542px,0 574px)"></div>
    <div class="layer band-purple" style="clip-path:polygon(10px 576px,368px 546px,368px 556px,10px 586px)"></div>
    <div class="layer rule-orange" style="clip-path:polygon(0 593px,528px 557px,528px 566px,0 602px)"></div>
    <div class="layer band-black" style="clip-path:polygon(0 602px,528px 566px,528px 742px,0 742px)"></div>

    <div class="apply" style="left:402px;width:108px;height:106px">
      <span class="apply__light" style="font-size:34px">APPLY</span>
      <span class="apply__bold" style="font-size:34px;margin-top:6px">NOW</span>
    </div>

    <h1 class="headline" style="left:22px;top:52px;transform:rotate(-4deg)">
      <span style="font-size:48px">Become a</span>
      <span style="font-size:53px;margin-top:6px">Mentor today</span>
    </h1>
    <p class="tagline" style="left:28px;top:186px;font-size:17px;white-space:nowrap;transform:rotate(-4.6deg)">Turn your skills and passion for music into a career</p>

    <p class="career" style="left:32px;top:506px;font-size:50px;transform:rotate(-5deg)">Start your career</p>

    <p class="audience" style="left:18px;top:618px;font-size:18px">Designed for musicians, artists, producers &amp; teachers</p>
    <ul class="contacts" style="left:18px;top:646px;font-size:13px">
      <li style="height:27px"><svg width="18" height="18"><use href="#icon-phone"/></svg><span style="margin-left:12px">Call 1300 XXX XXX</span></li>
      <li style="height:27px"><svg width="18" height="18"><use href="#icon-mail"/></svg><span style="margin-left:12px">youremail@meridianschoolofmusic.com.au</span></li>
      <li style="height:27px"><svg width="18" height="18"><use href="#icon-web"/></svg><span style="margin-left:12px">www.meridianschoolofmusic.com.au</span></li>
    </ul>
    <p class="brand" style="left:384px;top:680px;width:128px;font-size:22px">Meridian<br><span style="font-size:12px">School of Music</span></p>
  </section>

  <!-- Square post -->
  <section class="ad ad--square">
    <div class="layer photo" role="img" aria-label="Photo of two young musicians talking at a mixing desk in a recording studio"
         style="clip-path:polygon(0 130px,450px 94px,450px 336px,0 362px)"></div>
    <div class="layer band-purple" style="clip-path:polygon(0 0,450px 0,450px 88px,0 124px)"></div>
    <div class="layer rule-blue" style="clip-path:polygon(0 124px,450px 88px,450px 95px,0 131px)"></div>
    <div class="layer rule-white" style="clip-path:polygon(192px 262px,450px 242px,450px 248px,192px 268px)"></div>
    <div class="layer rule-orange" style="clip-path:polygon(192px 268px,450px 248px,450px 251px,192px 271px)"></div>
    <div class="layer rule-blue" style="clip-path:polygon(0 326px,300px 302px,300px 306px,0 330px)"></div>
    <div class="layer band-purple" style="clip-path:polygon(8px 333px,312px 309px,312px 317px,8px 341px)"></div>
    <div class="layer rule-orange" style="clip-path:polygon(0 355px,450px 330px,450px 338px,0 363px)"></div>
    <div class="layer band-black" style="clip-path:polygon(0 363px,450px 338px,450px 450px,0 450px)"></div>

    <div class="apply" style="left:370px;width:70px;height:70px">
      <span class="apply__light" style="font-size:22px">APPLY</span>
      <span class="apply__bold" style="font-size:22px;margin-top:4px">NOW</span>
    </div>

    <h2 class="headline" style="left:9px;top:22px;transform:rotate(-4.6deg)">
      <span style="font-size:37px">Become a</span>
      <span style="font-size:39px;margin-top:2px">Mentor today</span>
    </h2>
    <p class="tagline" style="left:13px;top:106px;font-size:14.5px;white-space:nowrap;transform:rotate(-4.8deg)">Turn your skills and passion for music into a career</p>

    <p class="career" style="left:24px;top:296px;font-size:39px;transform:rotate(-5deg)">Start your career</p>

    <p class="audience" style="left:8px;top:379px;font-size:12.5px">Designed for musicians, artists, producers &amp; teachers</p>
    <ul class="contacts" style="left:8px;top:399px;font-size:10px">
      <li style="height:16px"><svg width="12" height="12"><use href="#icon-phone"/></svg><span style="margin-left:8px">Call 1300 XXX XXX</span></li>
      <li style="height:16px"><svg width="12" height="12"><use href="#icon-mail"/></svg><span style="margin-left:8px">youremail@meridianschoolofmusic.com.au</span></li>
      <li style="height:16px"><svg width="12" height="12"><use href="#icon-web"/></svg><span style="margin-left:8px">www.meridianschoolofmusic.com.au</span></li>
    </ul>
    <p class="brand" style="left:346px;top:404px;width:96px;font-size:16px">Meridian<br><span style="font-size:9px">School of Music</span></p>
  </section>

  <!-- Wide banner -->
  <section class="ad ad--banner">
    <div class="layer photo" role="img" aria-label="Photo of two young musicians talking at a mixing desk in a recording studio"
         style="clip-path:polygon(184px 0,442px 0,442px 164px,244px 164px)"></div>
    <div class="layer rule-blue" style="clip-path:polygon(174px 0,184px 0,244px 164px,234px 164px)"></div>
    <div class="layer rule-white" style="clip-path:polygon(330px 108px,442px 100px,442px 105px,330px 113px)"></div>
    <div class="layer rule-orange" style="clip-path:polygon(330px 113px,442px 105px,442px 107px,330px 115px)"></div>
    <div class="layer rule-blue" style="clip-path:polygon(236px 146px,380px 134px,380px 137px,236px 149px)"></div>
    <div class="layer band-purple" style="clip-path:polygon(240px 151px,386px 139px,386px 145px,240px 157px)"></div>

    <div class="apply" style="left:392px;width:50px;height:50px">
      <span class="apply__light" style="font-size:15px">APPLY</span>
      <span class="apply__bold" style="font-size:15px;margin-top:3px">NOW</span>
    </div>

    <h2 class="headline" style="left:7px;top:10px;line-height:1.2">
      <span style="font-size:21px">Become a</span>
      <span style="font-size:21px">Mentor today</span>
    </h2>
    <p class="tagline" style="left:7px;top:66px;font-size:10.5px;white-space:nowrap">Turn your skills and passion for<br>music into a career</p>
    <p class="audience" style="left:7px;top:102px;font-size:7.8px">Designed for musicians, artists, producers &amp; teachers</p>
    <ul class="contacts contacts--banner" style="left:7px;top:114px;font-size:8.5px">
      <li style="height:14.5px"><svg width="9" height="9"><use href="#icon-phone"/></svg><span style="margin-left:5px">Call 1300 XXX XXX</span></li>
      <li style="height:14.5px"><svg width="9" height="9"><use href="#icon-mail"/></svg><span style="margin-left:5px">youremail@meridianschoolofmusic.com.au</span></li>
      <li style="height:14.5px"><svg width="9" height="9"><use href="#icon-web"/></svg><span style="margin-left:5px">www.meridianschoolofmusic.com.au</span></li>
    </ul>

    <p class="career" style="left:248px;top:128px;font-size:18px;transform:rotate(-5deg)">Start your career</p>
  </section>

</main>
</body>
</html>
```